Name of company is Raven Crest Shear Sharpening and Sales.Card design basic idea; I'm thinking back side just showing a sharp RAVEN CREST. Front side: I'm thinking a tiger showing teeth and claws.With the words "Raven Crest" larger type emphasized on one line.Then "Shear Sharpening and Sales" on the next line.Other info on front of card should be my name and phone #'s and address: Martin Kessling P (555)014-2287 CP (555)017-3365 My address is NOT to be emphasized.Can go at bottom of card. It is: 5072 Henley Court Larkfield NV 30417 If all that's too much to fit without looking cluttered than maybe the claw on the front with all the contact info. and just the Tiger on back of card. Whichever looks best.

Target Market(s)

Beauty Salons

Industry/Entity Type

It Company

Contact Information for Business Card

The 2 images,the claw and the tiger,could be either illustrations or photos.Whatever looks best.Got to be eye grabbing either way.

Requirements
Must have
• Contact info. Must be in color. And emphasize the identity. RAVEN CREST.Tiger on one side.Showing TEETH. Raven Crest on the other side. Showing the CLAW. .Both pics must emphasize SHARPNESS...This is a shear SHARPENING business. If one of the claw pics shows cutting grooves into something that's fine too. Card must show sharpness of the claw blade somehow.
Nice to have
• Attention grabbing. Images should jump off the card!
Should not have
• No boring cuddly tiger pics showing no teeth or claws or dull teeth or claws. No Black and whites.. No extra words other than what I've listed.

```html
<!DOCTYPE html>
<html lang="en">
<head>
<meta charset="utf-8">
<title>Raven Crest Shear Sharpening and Sales – Business Cards</title>
<link href="https://fonts.googleapis.com/css2?family=Tinos:wght@400;700&display=swap" rel="stylesheet">
<style>
  :root {
    --page-bg: #2b2b2d;
    --card-black: #050505;
    --text-white: #ffffff;
    --text-soft: #e6e6e6;
    --fur-orange: #b8692a;
    --fur-cream: #d9cbb4;
    --bark-brown: #6b4a36;
    --stone-grey: #8f8a82;
    --leaf-green: #6f7f52;
    --tiger-amber: #c77a2e;
  }
  * { margin: 0; padding: 0; box-sizing: border-box; }
  html, body {
    width: 1200px; height: 880px; overflow: hidden;
    background: var(--page-bg);
  }
  .sheet {
    width: 1200px; height: 880px;
    display: flex; flex-direction: column;
    align-items: center; justify-content: center; gap: 36px;
    font-family: "Tinos", "Times New Roman", serif;
  }
  .card {
    position: relative;
    width: 700px; height: 400px;
    border-radius: 22px;
    overflow: hidden;
    background: var(--card-black);
    box-shadow: 0 10px 28px rgba(0,0,0,.45);
  }

  /* Back side */
  .card-back .claw-photo {
    position: absolute; left: 0; top: 0; bottom: 0; width: 580px;
    background:
      radial-gradient(ellipse at 30% 25%, var(--bark-brown) 0%, transparent 45%),
      radial-gradient(ellipse at 65% 60%, var(--fur-orange) 0%, transparent 55%),
      radial-gradient(ellipse at 40% 70%, var(--fur-cream) 0%, transparent 50%),
      linear-gradient(160deg, #7a5a44 0%, #a9713d 45%, #cfc3b0 75%, var(--stone-grey) 100%);
  }
  .card-back .brand-band {
    position: absolute; right: 0; top: 0; bottom: 0; width: 120px;
    background: var(--card-black);
    display: flex; align-items: center; justify-content: center;
  }
  .card-back .brand-lockup {
    transform: rotate(90deg);
    white-space: nowrap;
    color: var(--text-white);
    text-align: left;
  }
  .brand-name {
    font-weight: 700;
    font-size: 44px;
    letter-spacing: 1px;
    line-height: 1;
  }
  .brand-tagline {
    font-weight: 700;
    font-size: 21px;
    line-height: 1.2;
    margin-top: 4px;
  }

  /* Front side */
  .card-front .tiger-photo {
    position: absolute; right: 0; top: 0; bottom: 0; width: 470px;
    background:
      radial-gradient(ellipse at 55% 45%, var(--tiger-amber) 0%, transparent 55%),
      radial-gradient(ellipse at 70% 20%, #e8d9bf 0%, transparent 40%),
      linear-gradient(120deg, var(--leaf-green) 0%, #9a6a36 50%, #c98a44 100%);
  }
  .card-front .photo-fade {
    position: absolute; left: 200px; top: 0; bottom: 0; width: 320px;
    background: linear-gradient(90deg, var(--card-black) 10%, rgba(5,5,5,0) 100%);
  }
  .card-front .contact-block {
    position: absolute; left: 44px; top: 92px;
    color: var(--text-white);
  }
  .card-front .brand-name { font-size: 50px; }
  .card-front .brand-tagline { font-size: 24px; margin-top: 2px; }
  .owner-name {
    font-weight: 700; font-size: 24px;
    margin: 34px 0 0 120px;
  }
  .contact-lines {
    margin: 40px 0 0 90px;
    font-size: 16px; line-height: 1.35;
    color: var(--text-soft);
  }
</style>
</head>
<body>
<main class="sheet">
  <section class="card card-back" aria-label="Card back">
    <div class="claw-photo" role="img" aria-label="Photo of a tiger gripping a branch with sharp extended claws"></div>
    <div class="brand-band">
      <div class="brand-lockup">
        <div class="brand-name">RAVEN CREST</div>
        <div class="brand-tagline">Shear Sharpening and Sales</div>
      </div>
    </div>
  </section>

  <section class="card card-front" aria-label="Card front">
    <div class="tiger-photo" role="img" aria-label="Photo of a snarling tiger showing its sharp teeth"></div>
    <div class="photo-fade"></div>
    <div class="contact-block">
      <div class="brand-name">RAVEN CREST</div>
      <div class="brand-tagline">Shear Sharpening and Sales</div>
      <div class="owner-name">Martin Kessling</div>
      <div class="contact-lines">
        <div class="phones">(555)014-2287 | (555)017-3365</div>
        <div class="address">CP 5072 Henley Court Larkfield NV 30417</div>
      </div>
    </div>
  </section>
</main>
</body>
</html>
```